Vacation/Holiday Home Wordpress Website

I currently have a website for our vacation/holiday rental home. It is 6 years old and needs a complete redesign to acommodate many new features available today. The existing website can be seen at www.quillfernstays.co.uk . The purpose of the website is mainly to provide useful infomation about our home, the destination of Barbados. The customer is also able to check availability and book. Please note that there is a booking element to the website which is hosted externally. This can be seen at

http://stay.reservo-grid.net/PickArrivalDay_Compact.asp?odta=kLP%3DQWRT%26ZXC%3DMNBV

I now wish to add key functionality such as:

- Video of property and area
- Customer video testimonials
- Other useful information

The navigation, menus and buttons need to be re designed to give a modern, innovative and professional look and feel.

My customers are mainly females between the ages of 35 and 55. The website needs to reassure customers who are parting with a lot of mony by booking online. It needs to give a sense of trust as this may be a once in a lifetime trip which they have saved up for for a long time. Many visitors to the website will be referred by other websites such as www.nestrove.co.uk and www.lodgemarket.co.uk.
Updates

Dear designers, 

Thank you for taking the time to write some further comments to you all. 

1. The homepage should have an availability search function as a key feature

2. The look and feel does NOT need to have the 3 feature columns like my current website has

3.  There should not be too much text on the homepage. Brief text can be included with 'more'  buttons to reveal more information 

4.  For designs that are under consideration, we will need to see a design for the other pages as they will be different to the homepage. Information from other pages on the existing website can be used. 

Reason: Dear all, I will be providing extensive feedback later today following a review that we have conducted with a group of our guests. To enable you to read and use this information, we have extended the deadline by 5 days. Thank you for the design submisions so far. We hope that the additional feedback will enable you to amend your designs appropriately. Regards Martin Hulbeck

Dear all,

Thank you for your designs.  I apologise that I am unable to give detailed feedback on each and every design submitted.  I will contact you individually and indicate whether we would like you to submit any further designs.  These should take into account the feedback below.

Feedback from design review group

1.  Logo should not be displayed in a white box.  It should blend in with the background or be overlayed onto the picture.

2.  There must be an availability calendar on the home page.

3.  Any background image should be subtle, maybe blurred and not distract from the main area.

4.  Text should be limited to a few key words with a 'read more' button to reveal more information.

5.  A gallery/slide show should be featured in the top part of the screen

6.  Icons can be used as navigation buttons

7.  Video testimonials is a key feature and should appear on the home page

8.   The use of bold and vibrant colours is preferred

9.   The 3 column format of the old website should not be copied

Regards

Martin

Target Market(s)

Female's, Families, 35 to 55 year olds, travellers to Barbados

Industry/Entity Type

Online

Requirements
Must have
• Pictures
Video
Testimonials
Clear and stylish navigation
Easy to use navigation
Should not have
• Dated look or feel

```html
<!DOCTYPE html>
<html lang="en">
<head>
<meta charset="utf-8">
<title>Quillfern Stays – Calvessa Holiday Home</title>
<link href="https://fonts.googleapis.com/css2?family=Signika:wght@400;600&family=PT+Sans:wght@400;700&family=Nunito:wght@800;900&display=swap" rel="stylesheet">
<style>
:root{
  --red:#e3361c;
  --red-dark:#c4220c;
  --blue:#0a5fb4;
  --blue-dark:#064a91;
  --panel:#2f2f2f;
  --ink:#333;
  --muted:#6d6d6d;
  --white:#fff;
  --field-border:#c9c9c9;
}
*{box-sizing:border-box;margin:0;padding:0}
html,body{width:1200px;height:970px;overflow:hidden}
body{position:relative;font-family:"PT Sans",sans-serif;color:var(--ink)}
.backdrop{position:absolute;inset:0;
  background:
    linear-gradient(90deg,rgba(0,0,0,0) 85%,rgba(58,110,40,.85) 92%,#4f7d33 100%),
    linear-gradient(180deg,#3f7fc9 0%,#9cc2e6 30%,#dfeaf3 45%,#3f9ab3 52%,#5fb0bf 62%,#e7dccb 78%,#f4efe8 100%);}
.site{position:absolute;left:117px;top:0;width:966px;height:970px}
.header{position:absolute;left:0;top:0;width:966px;height:117px;background:var(--white)}
.brand{position:absolute;left:33px;top:36px;display:flex;align-items:center;gap:10px}
.brand-dot{width:26px;height:26px;border-radius:50%;background:var(--red)}
.brand-name{font-family:"Signika",sans-serif;font-weight:600;font-size:27px;color:var(--red);letter-spacing:1px}
.social{position:absolute;right:11px;top:0;display:flex;gap:2px}
.social span{width:25px;height:26px;border-radius:0 0 13px 13px;background:#2b2b2b;display:block}
.phone{position:absolute;left:765px;top:59px;width:211px;height:39px;background:linear-gradient(var(--blue),var(--blue-dark));
  border-radius:3px 0 0 3px;color:var(--white);font-family:"Signika",sans-serif;font-size:23px;display:flex;align-items:center;padding-left:15px;gap:6px}
.nav{position:absolute;left:0;top:117px;width:966px;height:41px;background:linear-gradient(#ee4a26,var(--red-dark));display:flex}
.nav a{font-family:"Signika",sans-serif;font-weight:400;font-size:16.5px;color:var(--white);text-decoration:none;display:flex;align-items:center;justify-content:center;border-right:1px solid rgba(0,0,0,.12)}
.nav a.active{background:linear-gradient(#1a74cf,var(--blue-dark))}
.search{position:absolute;left:0;top:158px;width:333px;height:392px;background:var(--panel);color:var(--white)}
.search h1{position:absolute;left:31px;top:37px;font-family:"Signika",sans-serif;font-weight:400;font-size:30px;line-height:31px}
.search .lede{position:absolute;left:34px;top:118px;font-size:13px}
.field{position:absolute;background:var(--white);border:1px solid var(--field-border);color:#8a8a8a;font-size:14.5px;display:flex;align-items:center;padding-left:10px}
.field .cal{position:absolute;right:6px;top:5px}
.keyword{left:33px;top:143px;width:252px;height:34px;padding-left:13px;font-size:15px}
.keyword .go{position:absolute;right:0;top:0;width:44px;height:32px;background:var(--red);display:flex;align-items:center;justify-content:center}
.check{position:absolute;left:33px;top:301px;width:252px;height:43px;background:linear-gradient(#f14b28,var(--red-dark));border:1px solid #9c1a08;border-radius:2px;
  font-family:"Nunito",sans-serif;font-weight:900;font-size:19px;color:var(--white);display:flex;align-items:center;justify-content:center}
.advanced{position:absolute;right:52px;top:357px;font-size:13px}
.slider{position:absolute;left:333px;top:158px;width:633px;height:392px;overflow:hidden}
.slide-photo{position:absolute;inset:0;background:linear-gradient(135deg,#b7bdc4 0%,#d9dde1 40%,#eef0f2 60%,#8d96a5 78%,#c49a6c 100%)}
.arrow{position:absolute;top:171px;width:40px;height:40px;border-radius:50%;background:var(--white);display:flex;align-items:center;color:#555;font-size:18px;font-weight:700}
.arrow.prev{left:-20px;justify-content:flex-end;padding-right:6px}
.arrow.next{right:-20px;padding-left:6px}
.badge{position:absolute;left:36px;top:200px}
.slide-title{position:absolute;left:35px;top:290px;font-family:"Nunito",sans-serif;font-weight:900;font-size:35px;line-height:34px;color:var(--white);text-shadow:0 2px 4px rgba(0,0,0,.5);letter-spacing:-.5px}
.content{position:absolute;left:0;top:568px;width:966px;height:402px;background:var(--white);border-radius:4px 4px 0 0}
.card{position:absolute;top:31px;width:293px;height:181px;overflow:hidden}
.card .photo{position:absolute;inset:0}
.card .caption{position:absolute;left:0;bottom:0;width:100%;height:33px;background:rgba(40,40,40,.55);color:var(--white);font-family:"Signika",sans-serif;font-size:22px;padding-left:11px;line-height:33px}
.play{position:absolute;left:50%;top:90px;transform:translate(-50%,-50%);width:50px;height:50px;border-radius:50%;background:rgba(255,255,255,.35);border:4px solid #222;display:flex;align-items:center;justify-content:center}
.thumb{position:absolute;top:22px;width:83px;height:108px;background:var(--white)}
.thumb .img{height:84px}
.thumb p{font-family:"Signika",sans-serif;font-size:12.5px;text-align:center;line-height:24px;color:#222}
.footer{position:absolute;left:0;top:812px;width:966px;text-align:center}
.footer .brand-name{font-size:20px}
.footer nav{margin-top:18px;font-size:13px;color:var(--muted)}
.footer nav i{font-style:normal;color:#aaa;margin:0 4px}
.footer small{display:block;margin-top:8px;font-size:13px;color:var(--muted)}
</style>
</head>
<body>
<div class="backdrop" role="img" aria-label="Soft blurred tropical beach with sea, sky and palm foliage"></div>
<div class="site">
  <header class="header">
    <div class="brand"><span class="brand-dot"></span><span class="brand-name">Quillfern Stays</span></div>
    <div class="social"><span></span><span></span><span></span><span></span></div>
    <div class="phone">
      <svg width="18" height="20" viewBox="0 0 24 24"><path fill="#fff" d="M6.6 10.8a15 15 0 0 0 6.6 6.6l2.2-2.2c.3-.3.7-.4 1-.2 1.1.4 2.3.6 3.6.6.6 0 1 .4 1 1V20c0 .6-.4 1-1 1A17 17 0 0 1 3 4c0-.6.4-1 1-1h3.5c.6 0 1 .4 1 1 0 1.3.2 2.5.6 3.6.1.3 0 .7-.2 1z"/></svg>
      8008 555 017
    </div>
  </header>
  <nav class="nav">
    <a style="width:111px">Home</a>
    <a class="active" style="width:222px">Calvessa Holiday Home</a>
    <a style="width:125px">Local Area</a>
    <a style="width:121px">Book Now</a>
    <a style="width:94px">Prices</a>
    <a style="width:144px">Testimonials</a>
    <a style="width:149px;border-right:0">Contact us</a>
  </nav>
  <section class="search">
    <h1>Enjoy a Truly<br>Memorable Holiday</h1>
    <p class="lede">Search nomber of holiday homes worldwide</p>
    <div class="field keyword">Keyword
      <span class="go"><svg width="18" height="18" viewBox="0 0 20 20"><circle cx="8" cy="8" r="6" fill="none" stroke="#fff" stroke-width="2.4"/><path d="M12.5 12.5l5 5" stroke="#fff" stroke-width="2.6" stroke-linecap="round"/></svg></span>
    </div>
    <div class="field" style="left:33px;top:193px;width:121px;height:27px">Book Date
      <svg class="cal" width="18" height="17" viewBox="0 0 18 17"><rect x="1" y="2" width="16" height="14" fill="#999"/><g fill="#fff"><rect x="3" y="6" width="2" height="2"/><rect x="7" y="6" width="2" height="2"/><rect x="11" y="6" width="2" height="2"/><rect x="3" y="10" width="2" height="2"/><rect x="7" y="10" width="2" height="2"/><rect x="11" y="10" width="2" height="2"/></g></svg></div>
    <div class="field" style="left:163px;top:193px;width:122px;height:27px">Return Date
      <svg class="cal" width="18" height="17" viewBox="0 0 18 17"><rect x="1" y="2" width="16" height="14" fill="#999"/><g fill="#fff"><rect x="3" y="6" width="2" height="2"/><rect x="7" y="6" width="2" height="2"/><rect x="11" y="6" width="2" height="2"/><rect x="3" y="10" width="2" height="2"/><rect x="7" y="10" width="2" height="2"/><rect x="11" y="10" width="2" height="2"/></g></svg></div>
    <div class="field" style="left:33px;top:228px;width:121px;height:26px">Adults</div>
    <div class="field" style="left:163px;top:228px;width:122px;height:26px">Child</div>
    <div class="field" style="left:33px;top:263px;width:249px;height:26px">Bedrooms</div>
    <div class="check">Check Availability</div>
    <p class="advanced">Advanced Search&gt;&gt;</p>
  </section>
  <section class="slider">
    <div class="slide-photo" role="img" aria-label="Bright modern bedroom with a blue padded headboard, tall windows and sheer curtains"></div>
    <div class="arrow prev">&lsaquo;</div>
    <div class="arrow next">&rsaquo;</div>
    <svg class="badge" width="78" height="78" viewBox="0 0 78 78">
      <polygon fill="#e3261c" points="39,0 45,9 55,4 57,15 68,14 66,25 77,29 70,38 77,47 67,51 69,62 58,62 56,73 46,68 39,77 32,68 22,73 20,62 9,62 11,51 1,47 8,38 1,29 12,25 10,14 21,15 23,4 33,9"/>
      <text x="39" y="36" text-anchor="middle" fill="#fff" font-family="Nunito,sans-serif" font-weight="900" font-size="19">20%</text>
      <text x="39" y="55" text-anchor="middle" fill="#fff" font-family="Nunito,sans-serif" font-weight="900" font-size="19">OFF</text>
    </svg>
    <h2 class="slide-title">Calvessa - Stunning Home Close<br>to Coralmere / Palmvale Beach!</h2>
  </section>
  <section class="content">
    <article class="card" style="left:25px">
      <div class="photo" role="img" aria-label="Couple on a terrace overlooking the sea at sunset" style="background:linear-gradient(180deg,#c9a77c,#7a8fa3 55%,#3f5566)"></div>
      <div class="play"><svg width="16" height="18" viewBox="0 0 16 18"><path d="M2 1l13 8-13 8z" fill="#222"/></svg></div>
      <div class="caption">Our Video</div>
    </article>
    <article class="card" style="left:345px">
      <div class="photo" role="img" aria-label="Guests relaxing in white beach chairs on the sand" style="background:linear-gradient(180deg,#6fb6cf,#bfe0e6 50%,#e8e4dc)"></div>
      <div class="play"><svg width="16" height="18" viewBox="0 0 16 18"><path d="M2 1l13 8-13 8z" fill="#222"/></svg></div>
      <div class="caption">Guest Testimonials</div>
    </article>
    <article class="card" style="left:649px">
      <div class="photo" role="img" aria-label="Blurred tropical backdrop" style="background:linear-gradient(180deg,#2f6fb0,#8ab7d4 50%,#d8d2c6)"></div>
      <div class="thumb" style="left:14px"><div class="img" role="img" aria-label="Holiday villa exterior" style="background:linear-gradient(#2e6db8,#e5d8b8 60%,#4f8a3b)"></div><p>Holiday 1</p></div>
      <div class="thumb" style="left:104px"><div class="img" role="img" aria-label="Holiday home interior with garden view" style="background:linear-gradient(#f3efe6,#9fbf6a 55%,#b57f4f)"></div><p>Holiday 1</p></div>
      <div class="thumb" style="left:193px"><div class="img" role="img" aria-label="Wooden sun loungers by the sea" style="background:linear-gradient(#7cc4e0,#e9f2f5 45%,#c0703a)"></div><p>Holiday 1</p></div>
      <div class="caption">Some Holiday Homes</div>
    </article>
  </section>
  <footer class="footer">
    <div class="brand" style="position:static;justify-content:center"><span class="brand-dot" style="width:20px;height:20px"></span><span class="brand-name">Quillfern Stays</span></div>
    <nav>Home<i>/</i>Calvessa Holiday Home<i>/</i>Local Area<i>/</i>Book Now<i>/</i>Prices<i>/</i>Testimonials<i>/</i>Contact us</nav>
    <small>All right reserved copyright © 2013</small>
  </footer>
</div>
</body>
</html>
```